Package Storage Service

Ideas...

Business Name... "STASH IT AT BRENFORD":
Store it,
Don’t Ship it;
4-LESS
Convenience, Quality, Service

Easy as ABC…
A. Contact Us 062-455-3927
B. We deliver
C. We pick-up & Store

LESS, is the new MORE

Box Size* (Approx) Weight Limit Price per Month
41 cm X 34 cm X 26 cm 10 Kilos 12 CHFs/per month
48 cm X 43 cm X 35 cm 25 Kilos 25 CHFs/per month

* Larger sizes and prices available upon request.

Contact: Tom /062-455-3927

These are only ideas for a small package storage service for local college students. The storage times are usually for 1 - 3 months.
I need a catchy, creative, colorful design for a new business.

This flyer will need to be printable in color. A-4 size or 8 1/2 " X 11".

Target Market(s)

Hotel Management students leaving their program for vacations for short terms. They return after vacation or after practical work experiences 4 study.

Industry/Entity Type

College

Requirements
Must have
• Prices, box sizes, catchy format.

Idea will forward to their address should they not return to the school; for a postage fee + 15.00 CHFs.

Contact information for the PICKUP and DELIVERY Service... see above.

Include a PICKUP AND DELIVERY Option in the flyer.
Nice to have
• Colorful boxes with a creative idea for someone to choose spending a little each month rather than a lot at one time. 25 CHFs rather than 125 CHFs.
Should not have
• Not too wordy.

```html
<!DOCTYPE html>
<html lang="en">
<head>
<meta charset="utf-8">
<title>Stash It At Brenford – Package Storage Flyer</title>
<link rel="stylesheet" href="https://fonts.googleapis.com/css2?family=Russo+One&family=Carlito:wght@400;700&display=swap">
<style>
  :root {
    --stage: #e6e7e9;
    --paper: #ffffff;
    --brand-blue: #1f5fb4;
    --brand-green: #7ac143;
    --band-cyan: #27b8e6;
    --accent-yellow: #f5e61c;
    --ink: #111111;
    --label-green: #6cb33f;
    --photo-dark: #6b6a68;
    --photo-light: #c9b28c;
    --box-green: #8cc63f;
    --box-yellow: #fbb718;
    --box-pink: #ec4d9d;
  }
  * { margin: 0; padding: 0; box-sizing: border-box; }
  html, body { width: 1200px; height: 900px; overflow: hidden; background: var(--stage); }
  .flyer {
    position: absolute; left: 296px; top: 20px;
    width: 608px; height: 860px;
    background: var(--paper); overflow: hidden;
    box-shadow: 0 6px 24px rgba(0,0,0,.18);
    font-family: "Carlito", "Calibri", sans-serif;
  }
  .flyer-art { position: absolute; inset: 0; }
  .hero-photo {
    position: absolute; left: 0; top: 0; width: 608px; height: 330px;
    background: linear-gradient(160deg, var(--photo-dark) 0%, #8d8579 45%, var(--photo-light) 75%, #8a8783 100%);
  }
  .brand-title {
    position: absolute; left: 418px; top: 112px; width: 190px;
    font-family: "Russo One", sans-serif; font-size: 25px; line-height: 1.15;
    text-align: center;
  }
  .brand-title .line-one { color: var(--brand-blue); display: block; }
  .brand-title .line-two { color: var(--brand-green); display: block; }
  .slogan {
    position: absolute; left: 0; top: 332px; width: 560px; text-align: center;
    font-family: "Russo One", sans-serif; color: #fff;
  }
  .slogan .headline { font-size: 34px; display: block; }
  .slogan .values { font-size: 21px; display: block; margin-top: 4px; }
  .service-banner {
    position: absolute; left: 0; top: 447px; width: 540px; text-align: center;
    font-family: "Russo One", sans-serif; font-size: 24px; color: var(--accent-yellow);
  }
  .plans { position: absolute; left: 0; top: 500px; width: 608px; display: flex; }
  .plan { width: 202px; text-align: center; }
  .plan-box { width: 120px; height: 92px; margin: 0 auto 14px; border-radius: 4px; }
  .plan-box.green { background: var(--box-green); }
  .plan-box.yellow { background: var(--box-yellow); }
  .plan-box.pink { background: var(--box-pink); }
  .plan-label { font-weight: 700; font-size: 22px; color: var(--label-green); }
  .plan-value { font-size: 20px; color: var(--ink); line-height: 1.15; }
  .band-text {
    position: absolute; left: 0; width: 608px; text-align: center;
    font-family: "Russo One", sans-serif;
  }
  .band-text.request { top: 748px; font-size: 17px; color: var(--ink); }
  .band-text.call { top: 788px; font-size: 22px; color: var(--accent-yellow); }
  .band-text.contact { top: 829px; font-size: 18px; color: #12301a; }
</style>
</head>
<body>
  <main class="flyer">
    <div class="hero-photo" role="img" aria-label="Photo of a warehouse worker moving cardboard parcels along a roller conveyor"></div>
    <svg class="flyer-art" width="608" height="860" viewBox="0 0 608 860" aria-hidden="true">
      <polygon points="380,100 608,100 608,212 410,212" fill="#ffffff"/>
      <polygon points="0,300 400,300 412,318 0,318" fill="var(--brand-blue)"/>
      <polygon points="0,318 540,318 608,418 0,418" fill="var(--brand-green)"/>
      <polygon points="0,418 608,418 608,440 0,440" fill="var(--brand-blue)"/>
      <polygon points="0,440 560,440 530,486 0,486" fill="var(--band-cyan)"/>
      <polygon points="560,440 608,440 608,486 530,486" fill="var(--brand-blue)"/>
      <polygon points="0,740 560,740 530,780 0,780" fill="var(--brand-green)"/>
      <polygon points="0,780 608,780 608,820 0,820" fill="var(--brand-blue)"/>
      <polygon points="0,820 608,820 608,860 0,860" fill="var(--brand-green)"/>
    </svg>

    <h1 class="brand-title"><span class="line-one">STASH IT</span><span class="line-two">AT BRENFORD</span></h1>

    <p class="slogan"><span class="headline">Store it, Don’t Ship it;</span><span class="values">Convenience, Quality, Service</span></p>

    <p class="service-banner">PICKUP AND DELIVERY</p>

    <section class="plans">
      <div class="plan">
        <div class="plan-box green" role="img" aria-label="Illustration of an open green storage box"></div>
        <p class="plan-label">Box Size</p>
        <p class="plan-value">41cm x 34 cm x 26 cm<br>48 cm x 43 cm x 35 cm</p>
      </div>
      <div class="plan">
        <div class="plan-box yellow" role="img" aria-label="Illustration of an open yellow storage box"></div>
        <p class="plan-label">Weight Limit</p>
        <p class="plan-value">10 Kilos<br>25 Kilos</p>
      </div>
      <div class="plan">
        <div class="plan-box pink" role="img" aria-label="Illustration of an open pink storage box"></div>
        <p class="plan-label">Price Per Month</p>
        <p class="plan-value">12 CHFs/Per Month<br>25 CHFs/ Per Month</p>
      </div>
    </section>

    <p class="band-text request">Larger sizes and prices available upon request.</p>
    <p class="band-text call">Contact Us 062-455-3927</p>
    <p class="band-text contact">Contact: Tom /062-455-3927</p>
  </main>
</body>
</html>
```